Vina Lumbral

Lumbral embodies the purity and intensity of Chile’s cold coastal terroir. The sleek white label and bold X logo reflect the stark beauty and unrelenting nature of these extreme winemaking conditions. Crisp, vibrant, and refreshingly bold, Lumbral is a tribute to the wild energy of the Pacific winds and the cool embrace of the coastal valleys—a wine for those who seek purity and perfection in every sip. We would like to have a simple design focusing o the X, we try some option see attach but we are no satisfied is not enaguh eyes catching
Updates

Please create a mysterious, enigmatic label based on the typography and logo attached to the project. We need at least, at the entry level, five varietal products such as Carménère, Cabernet Sauvignon, Merlot, Chardonnay, and Malbec. Later, we would like to add more premium products, like a Reserva, a Special Reserva, or a Limited Edition. The design should be flexible and easily adaptable to accommodate various products while maintaining the same overall aesthetic.

I upload some wines label with printing technic we would like to use on our label, please incorporate this into your design

Project Brief – Large-Scale Brand Label Design
We are developing a new large-scale brand with a structured range of wines. Below are the key design elements and specifications for the labels:

Pinot Noir, Chardonnay, Syrah (Burgundy bottle shape – must include "Special Reserve" on the label)
General Label Guidelines
Year: Only mention "2024" (do not include the word “vintage”).
Capsules: Use standard-colored capsules only (no branding).
Label Design:
Focus on the label itself; bottle and background are irrelevant.
We can consider a wraparound label, but space must be reserved for back-label information.
Please refer to www.corlenti-wines.example for brand coherence. Let us know if further details are needed.

Target Market(s)

peopels who looking for simple design but strinking with the X . THe X could be like a painting brush somehting which make it look artistic

Industry/Entity Type

Wines producer

Font styles to use
Decorative
Script
Other font styles liked:
• the X would be nice if it look like he is Brush from a painter

Colors
0054AA
0677BA
7BADD7
CADEEF
E8F1F8
FFF300
FFF600
FEFA6F
FFFEC7
FFFEE8
EB3D1F
EC4F4E
F09395
F8D3D4
FCEDEE

Requirements
Must have
• We need to indicate the varietals Cabernet Sauvignon, the vintage 2024, the region DO Central Valley
Nice to have
• option on a burgendy bottle for chardonnay and pinot noir and option on bordeau bottle for Cabernet sauvignon and Merlot, We will need a large serie of 5 entrance lebvel (4 red one white) 2 reserve, 2 special reserve, 2 Limited

```html
<!DOCTYPE html>
<html lang="en">
<head>
<meta charset="utf-8">
<title>Lumbral – Cabernet Sauvignon Label</title>
<link rel="stylesheet" href="https://fonts.googleapis.com/css2?family=Gelasio:wght@400;600;700&family=Yellowtail&family=Kaushan+Script&display=swap">
<style>
  :root {
    --backdrop: #ecebe8;
    --label-white: #ffffff;
    --brand-red: #d81f2a;
    --ink: #1f1b1c;
    --rule-red: #d0202b;
  }
  * { margin: 0; padding: 0; box-sizing: border-box; }
  html, body {
    width: 1200px;
    height: 788px;
    overflow: hidden;
    background: var(--backdrop);
  }
  .canvas {
    position: relative;
    width: 1200px;
    height: 788px;
  }
  .wine-label {
    position: absolute;
    left: 320px;
    top: 24px;
    width: 560px;
    height: 740px;
    background: var(--label-white);
    box-shadow: 2px 3px 6px rgba(0, 0, 0, 0.25);
    color: var(--ink);
    overflow: hidden;
  }
  .rule-row {
    position: absolute;
    left: 0;
    right: 0;
    display: flex;
    align-items: center;
  }
  .rule-row .rule {
    flex: 1;
    height: 2px;
    background: var(--rule-red);
  }
  .region-row {
    top: 18px;
    height: 40px;
  }
  .region {
    font-family: "Yellowtail", "Kaushan Script", cursive;
    font-size: 34px;
    line-height: 40px;
    padding: 0 16px;
    color: var(--ink);
    white-space: nowrap;
  }
  .vintage {
    position: absolute;
    top: 62px;
    left: 0;
    right: 0;
    text-align: center;
    font-family: "Gelasio", serif;
    font-weight: 600;
    font-size: 20px;
    line-height: 24px;
    letter-spacing: 0.02em;
  }
  .brand-name {
    position: absolute;
    top: 262px;
    left: 0;
    right: 0;
    text-align: center;
    font-family: "Gelasio", serif;
    font-weight: 600;
    font-size: 120px;
    line-height: 150px;
    color: var(--brand-red);
    white-space: nowrap;
  }
  .varietal {
    position: absolute;
    top: 552px;
    left: 0;
    right: 0;
    text-align: center;
    font-family: "Gelasio", serif;
    font-weight: 600;
    font-size: 19px;
    line-height: 28px;
    letter-spacing: 0.5em;
    padding-left: 0.5em;
    white-space: nowrap;
  }
  .details-row {
    top: 658px;
    height: 32px;
  }
  .details {
    display: flex;
    align-items: center;
    padding: 0 12px;
    font-family: "Gelasio", serif;
    font-weight: 600;
    font-size: 21px;
    line-height: 32px;
    white-space: nowrap;
  }
  .details .divider {
    width: 1.5px;
    height: 30px;
    background: var(--ink);
    margin: 0 14px;
  }
</style>
</head>
<body>
  <main class="canvas">
    <section class="wine-label" aria-label="Lumbral Cabernet Sauvignon front label">
      <div class="rule-row region-row">
        <span class="rule"></span>
        <span class="region">Central Valley</span>
        <span class="rule"></span>
      </div>
      <p class="vintage">2024</p>

      <h1 class="brand-name">Lumbral</h1>

      <p class="varietal">CABERNET SAUVIGNON</p>

      <div class="rule-row details-row">
        <span class="rule"></span>
        <p class="details">
          <span class="volume">0.75 L</span>
          <span class="divider"></span>
          <span class="abv">Alc 12%</span>
        </p>
        <span class="rule"></span>
      </div>
    </section>
  </main>
</body>
</html>
```